Interior Design/ New Construction interior finishes

Interior Design Website

Target Market(s)

Home builders, New Construction, Renovations, Public

Industry/Entity Type

Construction

Coding

Coded - Design and coding required

Number of Pages Required

1 page

Font styles to use
Sans Serif

Colors

Designer to choose colors to be used in the design.

Requirements
Must have
• Section to upload pictures of projects
• Simple and modern design
• Designer 1 details about myself
• Logo
• Upload section for photos for future jobs
Nice to have
• Sections they can click on to see certain rooms in a house
• Decorating, floral arrangements, holiday decorating.
• I have lots of before and after as well. Maybe a section for those.

```html
<!DOCTYPE html>
<html lang="en">
<head>
<meta charset="utf-8">
<title>Lumen Interiors</title>
<link rel="stylesheet" href="https://fonts.googleapis.com/css2?family=Jost:wght@400;500;600;700&family=Open+Sans:ital,wght@0,400;0,600;0,700;1,400;1,600&display=swap">
<style>
:root{
  --ink:#1d1d1d;
  --dark:#232323;
  --panel:#2a2a2a;
  --grey:#8f8f8f;
  --mid:#5a5a5a;
  --light:#ededed;
  --white:#ffffff;
  --text:#444444;
  --head:"Jost",sans-serif;
  --body:"Open Sans",sans-serif;
}
*{box-sizing:border-box;margin:0;padding:0}
html,body{width:1200px;height:4000px;overflow:hidden;background:var(--white)}
body{position:relative;font-family:var(--body);color:var(--text)}
.abs{position:absolute}

/* header */
.site-header{left:0;top:0;width:1200px;height:120px;background:var(--white);z-index:3}
.site-header::before{content:"";position:absolute;left:0;top:0;width:1200px;height:3px;background:var(--ink)}
.nav-link{position:absolute;top:52px;font-family:var(--body);font-weight:700;font-size:15px;color:var(--ink);letter-spacing:.3px;text-transform:uppercase}
.brand-disc{left:480px;top:-32px;width:240px;height:240px;border-radius:50%;background:var(--white);z-index:3}
.brand-mark{left:570px;top:30px;width:60px;height:60px;border:3px solid var(--ink);border-radius:50%;z-index:4}
.brand-name{left:480px;top:106px;width:240px;text-align:center;font-family:var(--head);font-weight:400;font-size:28px;letter-spacing:2px;color:var(--ink);z-index:4}

/* hero */
.hero{left:0;top:120px;width:1200px;height:515px;background:linear-gradient(180deg,#6f6f6c 0%,#5d5b57 45%,#3d3a36 100%)}
.hero-title{left:0;top:275px;width:1200px;text-align:center;font-family:var(--head);font-weight:400;font-size:82px;letter-spacing:9px;color:var(--white)}
.hero-sub{left:0;top:396px;width:1200px;text-align:center;font-family:var(--head);font-weight:500;font-size:30px;color:var(--white)}
.hero-thumb{border-radius:50%;border:4px solid var(--white);background:linear-gradient(135deg,#b9b2a8,#7b746b)}

/* vertical labels */
.vertical-label{display:flex;align-items:center;justify-content:center;writing-mode:vertical-rl;font-family:var(--head);font-weight:500;font-size:28px;color:var(--white);letter-spacing:1px;white-space:nowrap}
.vertical-label.reads-up{transform:rotate(180deg)}

/* about */
.about-frame{left:99px;top:768px;width:405px;height:333px;background:var(--dark)}
.photo{border:3px solid var(--white);outline:1px solid #bdbdbd}
.about-photo{left:179px;top:805px;width:410px;height:262px;background:linear-gradient(135deg,#d9d4cd,#a99c8d 60%,#6e6559)}
.section-title{font-family:var(--head);font-weight:700;font-size:30px;color:var(--ink);letter-spacing:.5px}
.section-title .soft{color:var(--mid);font-weight:600}
.rule{height:3px;background:var(--ink)}
.about-copy{left:643px;top:852px;width:458px;font-size:14px;line-height:22px;color:var(--text)}
.about-copy p+p{margin-top:10px}
.btn-outline{left:643px;top:1045px;width:112px;height:48px;border:2px solid var(--ink);font-family:var(--body);font-weight:700;font-size:14px;line-height:44px;text-align:center;color:var(--ink)}

/* services */
.service{top:1211px;width:400px;height:333px;color:var(--white)}
.service-1{left:0;background:linear-gradient(135deg,#5b544c,#3a3530)}
.service-2{left:400px;background:linear-gradient(135deg,#262626,#141414)}
.service-3{left:800px;background:linear-gradient(135deg,#6b645c,#3e3934)}
.service-title{position:absolute;top:160px;font-family:var(--head);font-weight:700;font-size:27px;letter-spacing:.5px}
.service-text{position:absolute;top:210px;font-size:13.5px;line-height:21px;font-weight:600}
.service-icon{position:absolute;top:60px;width:74px;height:74px;border:3px solid var(--white);border-radius:50%}

/* before after */
.ba-dark{left:99px;top:1752px;width:405px;height:336px;background:var(--dark)}
.ba-grey{left:696px;top:1752px;width:405px;height:336px;background:var(--grey)}
.ba-photo-1{left:179px;top:1787px;width:410px;height:266px;background:linear-gradient(180deg,#f1f0ee,#dcdad6 65%,#b8b1a6)}
.ba-photo-2{left:611px;top:1787px;width:410px;height:266px;background:linear-gradient(180deg,#8d8a85,#a09c94 60%,#c9b56a)}
.ba-arrows{left:531px;top:1890px;width:138px;height:60px;border-radius:30px;background:var(--dark)}

/* projects */
.projects{left:0;top:2195px;width:1200px;height:645px;background:linear-gradient(180deg,#2b2b2b,#3b3936 55%,#2a2928)}
.project-card{background:var(--white);border:3px solid var(--white)}
.project-img{width:100%;background:linear-gradient(135deg,#e6e6e4,#a8a6a2)}
.project-label{font-family:var(--head);font-weight:500;font-size:22px;text-align:center;color:var(--ink)}
.project-card.is-active .project-label{background:var(--dark);color:var(--white)}

/* testimonials */
.testimonials{left:0;top:2840px;width:1200px;height:539px;background:var(--light)}
.quote-disc{left:547px;top:3014px;width:106px;height:106px;border-radius:50%;background:var(--dark)}
.quote-text{left:120px;top:3146px;width:960px;text-align:center;font-style:italic;font-weight:600;font-size:15px;line-height:30px;color:var(--ink)}
.quote-name{left:0;top:3226px;width:1200px;text-align:center;font-size:15px;font-weight:600;color:var(--ink)}
.dot{top:3286px;width:15px;height:15px;border-radius:50%;border:1.5px solid var(--ink)}
.dot.is-active{background:var(--ink)}

/* contact */
.contact{left:0;top:3379px;width:1200px;height:541px;background:linear-gradient(180deg,#2f2e2c,#46433f 50%,#2c2b29)}
.contact-photo{left:221px;top:3477px;width:414px;height:344px;background:linear-gradient(135deg,#cbbfb0,#8e7f6f 55%,#5a5048)}
.contact-form{left:635px;top:3477px;width:410px;height:344px;background:#121212}
.field{position:absolute;left:26px;width:335px;border-bottom:1.5px solid var(--white);font-family:var(--body);font-weight:600;font-size:15px;color:var(--white);padding-bottom:8px}
.btn-send{position:absolute;left:26px;top:262px;width:96px;height:40px;background:var(--white);color:var(--ink);font-size:13px;font-weight:600;text-align:center;line-height:40px}

/* footer */
.site-footer{left:0;top:3920px;width:1200px;height:80px;background:var(--white);text-align:center;line-height:80px;font-size:14px;font-weight:600;color:var(--ink)}
</style>
</head>
<body>

<header class="abs site-header">
  <nav>
    <span class="nav-link" style="left:99px">Home</span>
    <span class="nav-link" style="left:205px">About Us</span>
    <span class="nav-link" style="left:349px">Services</span>
    <span class="nav-link" style="left:762px">Before &amp; After Gallery</span>
    <span class="nav-link" style="left:1007px">Contact Us</span>
  </nav>
</header>
<div class="abs brand-disc"></div>
<div class="abs brand-mark"></div>
<div class="abs brand-name">Lumen Interiors</div>

<section class="abs hero" role="img" aria-label="Photo of a furnished living room with sofas and wooden coffee table"></section>
<h1 class="abs hero-title">LUMEN INTERIORS</h1>
<p class="abs hero-sub">Interior Finishes &amp; new construction company</p>
<div class="abs hero-thumb" style="left:464px;top:600px;width:70px;height:70px" role="img" aria-label="Thumbnail of living room"></div>
<div class="abs hero-thumb" style="left:557px;top:592px;width:86px;height:86px;background:linear-gradient(135deg,#8a8a8a,#3a3a3a)" role="img" aria-label="Thumbnail of dining room"></div>
<div class="abs hero-thumb" style="left:666px;top:600px;width:70px;height:70px;background:linear-gradient(135deg,#eeeeee,#b5b5b5)" role="img" aria-label="Thumbnail of bedroom"></div>

<section>
  <div class="abs about-frame"></div>
  <div class="abs vertical-label reads-up" style="left:116px;top:768px;width:46px;height:333px">INTERIOR FINISHES</div>
  <div class="abs photo about-photo" role="img" aria-label="Photo of a bright bathroom with freestanding tub"></div>
  <h2 class="abs section-title" style="left:643px;top:774px"><span class="soft">ABOUT</span> LUMEN INTERIORS</h2>
  <div class="abs rule" style="left:643px;top:826px;width:128px"></div>
  <div class="abs about-copy">
    <p>Nemo enim ipsam voluptatem quia voluptas sit aspernatur aut odit aut fugit, sed quia consequuntur magni dolores eos qui ratione voluptatem sequi nesciunt. Neque porro quisquam est, qui dolorem ipsum quia dolor sit amet, consectetur, adipisci velit, sed quia non numquam eius modi tempora.</p>
    <p>Neque porro quisquam est, qui dolorem ipsum quia dolor sit amet, consectetur, adipisci velit, sed quia non numquam eius modi tempora.</p>
  </div>
  <div class="abs btn-outline">READ MORE</div>
</section>

<section>
  <div class="abs service service-1" role="img" aria-label="Photo of a decorated living room">
    <div class="service-icon" style="left:277px"></div>
    <h3 class="service-title" style="right:48px">DECORATING</h3>
    <p class="service-text" style="right:48px;width:320px;text-align:right">Sed ut perspiciatis unde omnis iste natus error sit voluptatem accusan tium dolorem qualau dantium</p>
  </div>
  <div class="abs service service-2" role="img" aria-label="Photo of a dark dining space with floral arrangement">
    <div class="service-icon" style="left:263px"></div>
    <h3 class="service-title" style="left:0;width:400px;text-align:center">FLORAL ARRANGEMENTS</h3>
    <p class="service-text" style="left:48px;width:320px;text-align:right">Sed ut perspiciatis unde omnis iste natus error sit voluptatem accusan tium dolorem qualau dantium</p>
  </div>
  <div class="abs service service-3" role="img" aria-label="Photo of a staircase decorated for the holidays">
    <div class="service-icon" style="left:280px"></div>
    <h3 class="service-title" style="right:16px">HOLIDAY DECORATING</h3>
    <p class="service-text" style="right:48px;width:320px;text-align:right">Sed ut perspiciatis unde omnis iste natus error sit voluptatem accusan tium dolorem qualau dantium</p>
  </div>
</section>

<section>
  <h2 class="abs section-title" style="left:0;top:1626px;width:1200px;text-align:center"><span class="soft">BEFORE &amp;</span> AFTER</h2>
  <div class="abs rule" style="left:536px;top:1677px;width:128px"></div>
  <div class="abs ba-dark"></div>
  <div class="abs ba-grey"></div>
  <div class="abs vertical-label reads-up" style="left:118px;top:1752px;width:44px;height:336px">BEFORE</div>
  <div class="abs vertical-label" style="left:1036px;top:1752px;width:44px;height:336px">AFTER</div>
  <div class="abs photo ba-photo-1" role="img" aria-label="Before photo of a living room with grey sofa"></div>
  <div class="abs photo ba-photo-2" role="img" aria-label="After photo of a living room with yellow sofa"></div>
  <div class="abs ba-arrows">
    <svg width="138" height="60" viewBox="0 0 138 60" fill="none" stroke="#fff" stroke-width="3">
      <path d="M40 20 L30 30 L40 40"/><path d="M98 20 L108 30 L98 40"/>
      <line x1="69" y1="8" x2="69" y2="52" stroke="#555" stroke-width="1"/>
    </svg>
  </div>
</section>

<section class="abs projects" role="img" aria-label="Dark photo of a kitchen interior">
  <h2 class="section-title" style="position:absolute;left:0;top:64px;width:1200px;text-align:center;color:var(--white)">UPCOMING PROJECTS</h2>
  <div class="rule" style="position:absolute;left:554px;top:116px;width:92px;background:var(--white)"></div>
  <div class="project-card" style="position:absolute;left:112px;top:200px;width:288px;height:338px">
    <div class="project-img" style="height:280px" role="img" aria-label="Photo of an open-plan living area"></div>
    <div class="project-label" style="line-height:50px">NEMO ENIM IPSAM</div>
  </div>
  <div class="project-card is-active" style="position:absolute;left:443px;top:184px;width:314px;height:370px">
    <div class="project-img" style="height:306px;background:linear-gradient(135deg,#d8d8d6,#8d8b88)" role="img" aria-label="Photo of a bathroom vanity"></div>
    <div class="project-label" style="line-height:58px">NEMO ENIM IPSAM</div>
  </div>
  <div class="project-card" style="position:absolute;left:797px;top:200px;width:288px;height:338px">
    <div class="project-img" style="height:280px;background:linear-gradient(135deg,#ececea,#a4a29e)" role="img" aria-label="Photo of a bathroom with tub"></div>
    <div class="project-label" style="line-height:50px">NEMO ENIM IPSAM</div>
  </div>
  <svg style="position:absolute;left:36px;top:340px" width="24" height="40" fill="none" stroke="#fff" stroke-width="3"><path d="M20 4 L6 20 L20 36"/></svg>
  <svg style="position:absolute;left:1140px;top:340px" width="24" height="40" fill="none" stroke="#fff" stroke-width="3"><path d="M4 4 L18 20 L4 36"/></svg>
</section>

<section>
  <div class="abs testimonials"></div>
  <h2 class="abs section-title" style="left:0;top:2900px;width:1200px;text-align:center"><span class="soft">OUR</span> TESTIMONIALS</h2>
  <div class="abs rule" style="left:536px;top:2952px;width:128px"></div>
  <div class="abs quote-disc">
    <svg width="106" height="106" viewBox="0 0 106 106" fill="#fff">
      <path d="M32 60 q0-16 14-22 l2 5 q-8 4-8 10 h8 v16 h-16z"/>
      <path d="M56 60 q0-16 14-22 l2 5 q-8 4-8 10 h8 v16 h-16z"/>
    </svg>
  </div>
  <p class="abs quote-text">Sed ut perspiciatis unde omnis iste natus error sit voluptatem accusantium doloremque laudantium, totam rem aperiam, eaque ipsa quae ab illo inventore veritatis et quasi architecto beatae vitae dicta sunt explicabo.</p>
  <p class="abs quote-name">- Clara Weston</p>
  <span class="abs dot is-active" style="left:553px"></span>
  <span class="abs dot" style="left:573px"></span>
  <span class="abs dot" style="left:593px"></span>
  <span class="abs dot" style="left:613px"></span>
  <span class="abs dot" style="left:633px"></span>
</section>

<section class="abs contact" role="img" aria-label="Dark photo of a kitchen interior"></section>
<div class="abs contact-photo photo" role="img" aria-label="Photo of a bedroom with upholstered bench"></div>
<form class="abs contact-form">
  <div class="field" style="top:26px">Name *</div>
  <div class="field" style="top:76px">Email *</div>
  <div class="field" style="top:128px">Subject</div>
  <div class="field" style="top:180px;padding-bottom:26px">Message</div>
  <div class="btn-send">SEND NOW</div>
</form>

<footer class="abs site-footer">Copyrights @ 2018 Lumen Interiors. All Rights Reserved.</footer>

</body>
</html>
```